7 variations of an already existing packet design needed

i need 8 colour and flavour variations of a design that i have already in AI/PDF/PSD format

i need 7 colour variations of the packet with the names of the flavours incorporated onto the packaging itself.

the 7 colour/flavour variations i want are

pineapple
cherry
blueberry
bubblegum
strawberry
menthol
mango
Apple & Blackcurrant

Requirements
Must have
• Must use the original design and have different colour anf flavour variations as described in the brief.
Should not have
• Not be an original design

```html
<!DOCTYPE html>
<html lang="en">
<head>
<meta charset="utf-8">
<title>Flavoured Tobacco Packet Variations</title>
<link rel="stylesheet" href="https://fonts.googleapis.com/css2?family=Source+Sans+3:wght@600&family=PT+Serif&display=swap">
<style>
  :root {
    --canvas: #ffffff;
    --smoke-dark: #333333;
    --smoke-mid: #4a4a4a;
    --ink-light: #ffffff;
    --ink-dark: #2e2e2e;
    --menthol: #41bde8;
    --bubblegum: #2fba7c;
    --apple-blackcurrant: #4b0f5e;
    --strawberry-pink: #ec0c8c;
    --strawberry-red: #ec1c2e;
    --pineapple: #fcec40;
    --cherry: #ec1c2e;
    --mango: #fcaa50;
  }
  * { box-sizing: border-box; margin: 0; padding: 0; }
  html, body {
    width: 1200px;
    height: 1168px;
    overflow: hidden;
    background: var(--canvas);
  }
  .sheet { position: relative; width: 1200px; height: 1168px; }
  .packet {
    position: absolute;
    width: 350px;
    height: 370px;
    overflow: hidden;
  }
  .packet__smoke {
    position: absolute;
    inset: 0;
    background:
      radial-gradient(ellipse 45% 22% at 35% 30%, rgba(170,170,170,0.55), transparent 70%),
      radial-gradient(ellipse 40% 25% at 70% 28%, rgba(150,150,150,0.45), transparent 70%),
      radial-gradient(ellipse 55% 30% at 40% 70%, rgba(140,140,140,0.35), transparent 70%),
      radial-gradient(ellipse 70% 60% at 50% 50%, var(--smoke-mid), var(--smoke-dark));
  }
  .flavour-badge {
    position: absolute;
    left: 50%;
    top: 53%;
    width: 199px;
    height: 199px;
    margin: -99px 0 0 -99px;
    border-radius: 50%;
    text-align: center;
    color: var(--ink-light);
  }
  .flavour-badge--dark { color: var(--ink-dark); }
  .brand-name {
    position: absolute;
    left: 0; right: 0;
    top: 56px;
    font-family: "Source Sans 3", sans-serif;
    font-weight: 600;
    font-size: 19px;
    line-height: 1;
    letter-spacing: 1px;
    text-transform: uppercase;
  }
  .flavour-block {
    position: absolute;
    left: 0; right: 0;
    top: 108px;
    display: flex;
    flex-direction: column;
    align-items: center;
  }
  .flavour-name {
    font-family: "Source Sans 3", sans-serif;
    font-weight: 600;
    font-size: 27px;
    line-height: 1;
    letter-spacing: -0.3px;
    text-transform: uppercase;
  }
  .flavour-name--small { font-size: 20px; line-height: 1.05; }
  .flavour-type {
    font-family: "PT Serif", serif;
    font-size: 15px;
    line-height: 1.1;
  }
  .badge--apple .brand-name { top: 48px; }
  .badge--apple .flavour-block { top: 92px; }
  .badge--menthol { background: var(--menthol); }
  .badge--bubblegum { background: var(--bubblegum); }
  .badge--apple { background: var(--apple-blackcurrant); }
  .badge--strawberry-pink { background: var(--strawberry-pink); }
  .badge--strawberry-red { background: var(--strawberry-red); }
  .badge--pineapple { background: var(--pineapple); }
  .badge--cherry { background: var(--cherry); }
  .badge--mango { background: var(--mango); }
</style>
</head>
<body>
<main class="sheet">

  <section class="packet" style="left:439px; top:22px;">
    <div class="packet__smoke" role="img" aria-label="Soft grey smoke background photograph"></div>
    <div class="flavour-badge badge--menthol">
      <span class="brand-name">Harbor Leaf</span>
      <div class="flavour-block">
        <span class="flavour-name">Menthol</span>
        <span class="flavour-type">flavoured tobacco</span>
      </div>
    </div>
  </section>

  <section class="packet" style="left:808px; top:22px;">
    <div class="packet__smoke" role="img" aria-label="Soft grey smoke background photograph"></div>
    <div class="flavour-badge badge--bubblegum">
      <span class="brand-name">Harbor Leaf</span>
      <div class="flavour-block">
        <span class="flavour-name">Bubblegum</span>
        <span class="flavour-type">flavoured tobacco</span>
      </div>
    </div>
  </section>

  <section class="packet" style="left:74px; top:405px;">
    <div class="packet__smoke" role="img" aria-label="Soft grey smoke background photograph"></div>
    <div class="flavour-badge badge--apple">
      <span class="brand-name">Harbor Leaf</span>
      <div class="flavour-block">
        <span class="flavour-name flavour-name--small">Apple &amp;<br>Blackcurrant</span>
        <span class="flavour-type">flavoured tobacco</span>
      </div>
    </div>
  </section>

  <section class="packet" style="left:437px; top:405px;">
    <div class="packet__smoke" role="img" aria-label="Soft grey smoke background photograph"></div>
    <div class="flavour-badge badge--strawberry-pink">
      <span class="brand-name">Harbor Leaf</span>
      <div class="flavour-block">
        <span class="flavour-name">Strawberry</span>
        <span class="flavour-type">flavoured tobacco</span>
      </div>
    </div>
  </section>

  <section class="packet" style="left:808px; top:405px;">
    <div class="packet__smoke" role="img" aria-label="Soft grey smoke background photograph"></div>
    <div class="flavour-badge badge--strawberry-red">
      <span class="brand-name">Harbor Leaf</span>
      <div class="flavour-block">
        <span class="flavour-name">Strawberry</span>
        <span class="flavour-type">flavoured tobacco</span>
      </div>
    </div>
  </section>

  <section class="packet" style="left:68px; top:787px;">
    <div class="packet__smoke" role="img" aria-label="Soft grey smoke background photograph"></div>
    <div class="flavour-badge flavour-badge--dark badge--pineapple">
      <span class="brand-name">Harbor Leaf</span>
      <div class="flavour-block">
        <span class="flavour-name">Pineapple</span>
        <span class="flavour-type">flavoured tobacco</span>
      </div>
    </div>
  </section>

  <section class="packet" style="left:439px; top:787px;">
    <div class="packet__smoke" role="img" aria-label="Soft grey smoke background photograph"></div>
    <div class="flavour-badge badge--cherry">
      <span class="brand-name">Harbor Leaf</span>
      <div class="flavour-block">
        <span class="flavour-name">Cherry</span>
        <span class="flavour-type">flavoured tobacco</span>
      </div>
    </div>
  </section>

  <section class="packet" style="left:805px; top:787px;">
    <div class="packet__smoke" role="img" aria-label="Soft grey smoke background photograph"></div>
    <div class="flavour-badge badge--mango">
      <span class="brand-name">Harbor Leaf</span>
      <div class="flavour-block">
        <span class="flavour-name">Mango</span>
        <span class="flavour-type">flavoured tobacco</span>
      </div>
    </div>
  </section>

</main>
</body>
</html>
```